Brochure layout for a small country church

St. Aldric is a small country church located on the central coast of CA. Last year our priest retired, and we are in the process of seeking a new church leader. To support our search process, we created a profile brochure that describes who we are in words and images.

The copy has been carefully written and fully edited, and we have gathered, tagged and foldered high-resolution images. We now need a person with your talents to arrange the words and pictures for us!

This document, which we call a 'profile' but is actually a brochure, will be in PDF format, size 8.5x11, for web display and local printing only. It will be posted on a national database and be shared with candidates by email and on our website. We do not intend to reproduce this on paper, though we expect some users will print pages on their printers.

Here is a Filevault link to access the copy, images and layout instructions:
https://www.filevaultshare.example/sh/k3rtwq8zplm7x1n/BBQZRE-19k84_pL2NwTyeHoRk

The layout instructions include specific information on image placement, and gives you much flexibility to arrange the copy/images the way you think looks best. All we ask is that you do not change the copy.

Images may be processed, cropped, inverted, enhanced … whatever you think looks right. We tried to give you the largest images possible, so you can get good resolution on the page.

Please do not let the length of the document concern you … you can cut/paste the copy, using any serif font that matches the look/feel of our church, and all of the images have been tagged and folder addressed in the document so you know where to find them. Page count does not matter as long as it looks good, and once you start laying out the pages it should not take long to finish. We just need someone with your design skills to make it look good!

As we stated in the copy narrative, we are a warm, loving and inclusive parish that is humble, happy and grateful for the many blessings we have. Our greatest quality is our people. In your design work, anything you can do to bring forward these values will be appreciated.

If you have any questions, please do not hesitate to contact me (Darren Pulsby/darren@darrenpulsby.example) and I will answer them for you right away.

Thank you for considering our brochure project, and we look forward to your submission.

```html
<!DOCTYPE html>
<html lang="en">
<head>
<meta charset="UTF-8">
<title>St. Aldric Parish Profile — Table of Contents</title>
<link rel="stylesheet" href="https://fonts.googleapis.com/css2?family=Lato:wght@300;700&display=swap">
<style>
  :root {
    --page-bg: #eee8dd;
    --page-bg-light: #f3eee6;
    --pill-brown: #5a3a1d;
    --text-brown: #6e4d2e;
    --glass-rose: #e7b9a3;
    --glass-peach: #f0cdb8;
    --glass-blue: #8fb6d6;
    --wood-dark: #2a1a10;
    --wood-mid: #5a3a24;
    --white: #ffffff;
  }
  * { margin: 0; padding: 0; box-sizing: border-box; }
  html, body {
    width: 927px;
    height: 1200px;
    overflow: hidden;
    background: var(--page-bg);
  }
  .page {
    position: relative;
    width: 927px;
    height: 1200px;
    background: linear-gradient(180deg, var(--page-bg-light) 0%, var(--page-bg) 100%);
    overflow: hidden;
  }
  .hero-photo {
    position: absolute;
    top: 0;
    left: 0;
    width: 927px;
    height: 565px;
    background:
      linear-gradient(180deg, rgba(238,232,221,0) 55%, rgba(238,232,221,0.85) 88%, var(--page-bg-light) 100%),
      radial-gradient(ellipse 120px 110px at 210px 95px, rgba(143,182,214,0.55), rgba(143,182,214,0) 100%),
      linear-gradient(90deg, var(--glass-peach) 0%, var(--glass-rose) 30%, #d9b3a0 40%, var(--wood-mid) 46%, var(--wood-dark) 62%, #3b271a 80%, #6a5444 100%);
  }
  .contents {
    position: absolute;
    top: 574px;
    left: 0;
    width: 927px;
    text-align: center;
  }
  .contents-title {
    display: inline-block;
    width: 359px;
    height: 41px;
    line-height: 41px;
    border-radius: 21px;
    background: var(--pill-brown);
    color: var(--white);
    font-family: "Lato", sans-serif;
    font-weight: 700;
    font-size: 28px;
    letter-spacing: 0.2px;
  }
  .contents-list {
    list-style: none;
    margin-top: 11px;
    font-family: "Lato", sans-serif;
    font-weight: 300;
    font-size: 23px;
    line-height: 30.6px;
    color: var(--text-brown);
  }
</style>
</head>
<body>
  <main class="page">
    <div class="hero-photo" role="img" aria-label="Photograph of a stained glass window with a red and blue roundel beside a row of tall white altar candles in brass holders"></div>
    <section class="contents">
      <h1 class="contents-title">TABLE OF CONTENTS</h1>
      <ul class="contents-list">
        <li>Introduction</li>
        <li>Who We Are</li>
        <li>The Rector We Seek</li>
        <li>Looking Forward</li>
        <li>Our Community</li>
        <li>History</li>
        <li>Facilities</li>
        <li>Worship and Music</li>
        <li>Parish Life</li>
        <li>Lay Ministry</li>
        <li>Governance</li>
        <li>Pastoral Care</li>
        <li>Outreach Fellowship</li>
        <li>Parish Demographics</li>
        <li>Children and Youth Ministry</li>
        <li>Stewardship</li>
        <li>Finances</li>
        <li>Contact Information</li>
      </ul>
    </section>
  </main>
</body>
</html>
```